Creative 1 page website design with html coding needed to go with Game Pre-Registration App

Early Bird Lounge
~Discover games before release~

Website keywords: Simple, slick, stylish
Colors: Black, white, pink (like our logo)

***draft can be created in PSD or HTML***

We have a brand new service called Early Bird Lounge which will be a game app pre-registration service. We already have the icon & UI for the app and we are looking for a slick & stylish corporate website to go with the service.

This will be a corporate website aim for businesses to contact us. Consumers will not be able to pre-register for games here. We do however want consumers to download our app from Nimbus Arcade after landing here.

Some framework we have in mind for 1 page website:
Home - default page showing the UI of the app and Nimbus Arcade icon with store link.
Our Service - quick explanation about our service & it's strength
Clients - logos of our clients
Press-
Pricing - basic usage is free. There will be premium services customers can use on a performance basis (CPA).
Contact Us

Call to action will be 1. Download the app 2. Contact us

We would like to be able to edit the press and clients section with web developer's support.

website in image:
https://www.velquorin.com/

Target Market(s)

Marketing managers of game developer. We want game developers to find out about our service and get in touch with us. The service will only be available in USA.

Midcore gamers in USA: Our end users will be game enthusiasts from US. Male aged 15-35.

Industry/Entity Type

Games

Font styles to use
Sans Serif

Colors
000000
ffffff
e567a6
e34097

Requirements
Must have
• - Only use our colors from the logo attached.
- UI of our app with an Zephyx phone
- Link to Nimbus Arcade Store
- slick & modern design
- Font used: Century Gothic

```html
<!DOCTYPE html>
<html lang="en">
<head>
<meta charset="utf-8">
<title>Early Bird Lounge – Our Services</title>
<link rel="stylesheet" href="https://fonts.googleapis.com/css2?family=Questrial&display=swap">
<style>
  :root {
    --ink: #ffffff;
    --ink-soft: rgba(255, 255, 255, 0.9);
    --pink: #e34097;
    --pink-light: #e567a6;
    --black: #000000;
    --dot-fill: #1a0612;
  }
  * { box-sizing: border-box; margin: 0; padding: 0; }
  html, body {
    width: 1200px;
    height: 669px;
    overflow: hidden;
    background: var(--black);
  }
  .services {
    position: relative;
    width: 1200px;
    height: 669px;
    overflow: hidden;
    font-family: "Questrial", "Century Gothic", sans-serif;
    color: var(--ink);
  }
  .services__backdrop {
    position: absolute;
    inset: 0;
    background:
      radial-gradient(circle 60px at 300px 560px, rgba(227, 64, 151, 0.45), transparent 100%),
      radial-gradient(circle 45px at 470px 600px, rgba(229, 103, 166, 0.35), transparent 100%),
      radial-gradient(circle 55px at 640px 330px, rgba(227, 64, 151, 0.30), transparent 100%),
      radial-gradient(ellipse 40% 35% at 88% 10%, rgba(227, 64, 151, 0.40), transparent 70%),
      radial-gradient(ellipse 55% 60% at 0% 0%, rgba(227, 64, 151, 0.75), transparent 75%),
      linear-gradient(120deg, #8a1f5e 0%, #4a0f32 35%, #22061a 65%, var(--black) 100%);
  }
  .services__title {
    position: absolute;
    top: 30px;
    left: 0;
    width: 100%;
    text-align: center;
    font-size: 30px;
    font-weight: 400;
    font-style: italic;
    letter-spacing: 0.5px;
  }
  .service {
    position: absolute;
    display: flex;
    align-items: center;
    gap: 34px;
  }
  .service--ideas { top: 100px; left: 160px; }
  .service--team { top: 268px; left: 150px; }
  .service--global { top: 440px; left: 110px; }
  .service__icon {
    width: 64px;
    height: 64px;
    flex: none;
  }
  .service__text {
    width: 740px;
    font-size: 16px;
    font-style: italic;
    line-height: 1.45;
    text-align: center;
    color: var(--ink-soft);
  }
  .section-nav {
    position: absolute;
    top: 250px;
    left: 1090px;
    width: 14px;
    height: 110px;
  }
</style>
</head>
<body>
<main class="services">
  <div class="services__backdrop" role="img" aria-label="Soft pink bokeh lights on a black backdrop with a faint dotted world map glow"></div>

  <h1 class="services__title">Our Services</h1>

  <section class="service service--ideas">
    <svg class="service__icon" viewBox="0 0 70 70" aria-hidden="true" fill="none" stroke="var(--ink)" stroke-width="3" stroke-linecap="round">
      <path d="M27 46c0-6-7-10-7-18a15 15 0 0 1 30 0c0 8-7 12-7 18z"/>
      <line x1="28" y1="51" x2="42" y2="51"/>
      <line x1="30" y1="56" x2="40" y2="56"/>
      <line x1="35" y1="4" x2="35" y2="8"/>
      <line x1="12" y1="13" x2="15" y2="16"/>
      <line x1="58" y1="13" x2="55" y2="16"/>
      <line x1="5" y1="30" x2="9" y2="30"/>
      <line x1="61" y1="30" x2="65" y2="30"/>
    </svg>
    <p class="service__text">This is Pixelmarch's version of Lorem Ipsum. Proin gravida nibh vel velit auctor aliquet. Aenean sollicitudin, lorem quis bibendum auctor, nisi elit consequat ipsum, nec sagittis sem nibh id elit. Duis sed odio sit amet nibh vulputate cursus a sit amet mauris. Morbi accumsan ipsum velit. Nam nec tellus a odio tincidunt auctor a ornare odio. Sed non mauris vitae erat consequat auctor eu in elit. Class aptent taciti sociosqu ad litora</p>
  </section>

  <section class="service service--team">
    <p class="service__text">This is Pixelmarch's version of Lorem Ipsum. Proin gravida nibh vel velit auctor aliquet. Aenean sollicitudin, lorem quis bibendum auctor, nisi elit consequat ipsum, nec sagittis sem nibh id elit. Duis sed odio sit amet nibh vulputate cursus a sit amet mauris. Morbi accumsan ipsum velit. Nam nec tellus a odio tincidunt auctor a ornare odio. Sed non mauris vitae erat consequat auctor eu in elit. Class aptent taciti sociosqu ad litora</p>
    <svg class="service__icon" viewBox="0 0 70 70" aria-hidden="true" fill="var(--ink)">
      <circle cx="35" cy="22" r="10"/>
      <circle cx="16" cy="30" r="7"/>
      <circle cx="54" cy="30" r="7"/>
      <path d="M18 54c0-11 8-18 17-18s17 7 17 18z"/>
      <path d="M4 54c0-8 5-14 12-14 3 0 5 1 7 2-4 3-6 7-7 12z"/>
      <path d="M66 54c0-8-5-14-12-14-3 0-5 1-7 2 4 3 6 7 7 12z"/>
    </svg>
  </section>

  <section class="service service--global">
    <svg class="service__icon" viewBox="0 0 70 70" aria-hidden="true" fill="none" stroke="var(--ink)" stroke-width="3">
      <circle cx="35" cy="35" r="27" fill="rgba(255,255,255,0.15)"/>
      <ellipse cx="35" cy="35" rx="12" ry="27"/>
      <line x1="8" y1="35" x2="62" y2="35"/>
      <path d="M12 22h46M12 48h46"/>
    </svg>
    <p class="service__text">This is Pixelmarch's version of Lorem Ipsum. Proin gravida nibh vel velit auctor aliquet. Aenean sollicitudin, lorem quis bibendum auctor, nisi elit consequat ipsum, nec sagittis sem nibh id elit. Duis sed odio sit amet nibh vulputate cursus a sit amet mauris. Morbi accumsan ipsum velit. Nam nec tellus a odio tincidunt auctor a ornare odio. Sed non mauris vitae erat consequat auctor eu in elit. Class aptent taciti sociosqu ad litora</p>
  </section>

  <svg class="section-nav" viewBox="0 0 14 110" aria-label="Section navigation" fill="none" stroke="var(--ink)" stroke-width="1.5">
    <line x1="7" y1="12" x2="7" y2="98" stroke-opacity="0.5"/>
    <circle cx="7" cy="7" r="4" fill="var(--dot-fill)"/>
    <circle cx="7" cy="31" r="4" fill="var(--ink)"/>
    <circle cx="7" cy="55" r="4" fill="var(--dot-fill)"/>
    <circle cx="7" cy="79" r="4" fill="var(--dot-fill)"/>
    <circle cx="7" cy="103" r="4" fill="var(--dot-fill)"/>
  </svg>
</main>
</body>
</html>
```